Stroke Process

I need to create an infographic design that can help me explain the process of a new project that I am working on. The project is a step by step illustration on what needs to be done in order to get a stroke patient that proper wheelchair.

The graphics should walk a client through the process starting with #1 in the inpatient process and the explanation of the steps through the last step in the outpatient process. I uploaded two documents but the document with the explanation is the document to build the illustration on. This is a healthcare piece so the graphics should represent healthcare

```html
<!DOCTYPE html>
<html lang="en">
<head>
<meta charset="utf-8">
<title>Stroke Patient Process</title>
<link rel="stylesheet" href="https://fonts.googleapis.com/css2?family=Oswald:wght@500;600&family=Open+Sans:wght@400;600;700;800&display=swap">
<style>
  :root {
    --band: #3f7fd3;
    --band-dark: #2c63b3;
    --step: #4d87d5;
    --navy: #1b3a78;
    --ink: #2b2b2b;
    --white: #ffffff;
    --paper: #ffffff;
    --accent: #5b8fd8;
  }
  * { margin: 0; padding: 0; box-sizing: border-box; }
  html, body { width: 1200px; height: 5070px; overflow: hidden; background: var(--paper); }
  body { position: relative; font-family: "Open Sans", Arial, sans-serif; color: var(--ink); font-size: 20px; line-height: 1.35; }
  .abs { position: absolute; }

  .title-band { left: 0; top: 0; width: 1200px; height: 130px; background: var(--band); display: flex; align-items: center; justify-content: center; }
  .title-band h1 { font-family: "Oswald", Arial Narrow, sans-serif; font-weight: 600; color: var(--white); font-size: 92px; letter-spacing: 1px; line-height: 1; }
  .stripe { left: 0; width: 1200px; height: 22px; background: repeating-linear-gradient(135deg, var(--band) 0 10px, var(--band-dark) 10px 20px); }

  .section-head { font-family: "Oswald", Arial Narrow, sans-serif; font-weight: 600; color: var(--navy); font-size: 44px; line-height: 1; }
  .intro { left: 60px; top: 270px; width: 1080px; font-size: 21px; line-height: 1.38; }

  .step { left: 60px; width: 630px; background: var(--step); color: var(--white); padding: 28px 34px; }
  .step-num { position: absolute; left: 24px; top: 24px; width: 64px; height: 72px; background: var(--white); color: var(--navy); font-family: "Oswald", sans-serif; font-size: 56px; display: flex; align-items: center; justify-content: center; }
  .step-title { margin-left: 80px; font-weight: 700; font-size: 21px; min-height: 72px; display: flex; align-items: center; }
  .step ul { list-style: none; margin-top: 14px; }
  .step li { position: relative; padding-left: 24px; margin-bottom: 6px; font-size: 20px; }
  .step li::before { content: "•"; position: absolute; left: 0; }
  .step .big { font-size: 34px; }
  .art { position: absolute; border-radius: 6px; }

  .side { left: 720px; width: 440px; font-size: 20px; }
  .side h3 { font-weight: 700; font-size: 21px; color: var(--ink); }
  .side ul { list-style: none; margin-top: 12px; }
  .side li { position: relative; padding-left: 24px; margin-bottom: 8px; }
  .side li::before { content: "•"; position: absolute; left: 0; }
  .side ul ul { margin-top: 4px; }
  .neuro-label { color: var(--accent); font-weight: 700; text-align: center; }
  .icon-circle { width: 110px; height: 110px; border-radius: 50%; background: var(--band-dark); margin: 14px auto; }
</style>
</head>
<body>
  <header class="abs title-band"><h1>STROKE PATIENT PROCESS</h1></header>
  <div class="abs stripe" style="top:130px"></div>

  <h2 class="abs section-head" style="left:60px;top:200px;font-size:40px">REASON FOR FOLLOWING PROCESS RECOMMENDATIONS:</h2>
  <p class="abs intro">Medicare stroke clients are often discharged before it can be ascertained which mobility equipment will best suit their mobility needs and allow them to perform/ participate in their Activities of Daily Living. Yet they require a wheelchair to be discharged. There a rental chair is currently requested which can cause many issues when trying to get Medicare to approve appropriate mobility equipment when specific client issues can be ascertained and documented.</p>

  <h2 class="abs section-head" style="left:60px;top:510px">IN PATIENT PROCESS</h2>

  <!-- In patient step 1 -->
  <section class="abs step" style="top:580px;height:490px">
    <div class="step-num">1</div>
    <div class="step-title">Patient admitted into Facility With CVA left or right side</div>
    <ul>
      <li><span class="big">46,000</span> diagnosis in Southern California</li>
      <li><span class="big">25%</span> Hemiplegia or Hemiparesis</li>
    </ul>
    <div class="art" role="img" aria-label="Illustration of a hospital building with an ambulance" style="left:90px;top:270px;width:420px;height:190px;background:linear-gradient(#cfe3f7,#7fb0e6)"></div>
  </section>
  <aside class="abs side" style="top:590px">
    <p class="neuro-label">Neurological Conditions</p>
    <h3 style="margin-top:10px">Hemiplegia:</h3>
    <p>Paralysis on one side of the body</p>
    <div class="icon-circle" role="img" aria-label="Icon of a paralysed arm"></div>
    <h3>Hemiparesis:</h3>
    <p>Weakness on one side of the body.</p>
    <div class="icon-circle" role="img" aria-label="Icon of a weakened arm"></div>
  </aside>

  <!-- In patient step 2 -->
  <section class="abs step" style="top:1115px;height:225px">
    <div class="step-num">2</div>
    <div class="step-title">Diagnosed with Hemiplegia or Hemiparesis</div>
    <p style="margin-top:10px">R26.81 &nbsp;Gait Instability<br>I681.90 &nbsp;Hemiplegia &nbsp;OR<br>I69.354 &nbsp;Hemiparesis<br>I69.90 &nbsp;&nbsp;Late effects of CVA (Cerebrovascular Accident)</p>
  </section>
  <aside class="abs side" style="top:1120px">
    <p><strong>Send:</strong> &nbsp;Mobility Allies<br>&nbsp;&nbsp;&nbsp;&nbsp;&nbsp;&nbsp;&nbsp;&nbsp;&nbsp;&nbsp;&nbsp;800.555.0142<br>&nbsp;&nbsp;&nbsp;&nbsp;&nbsp;&nbsp;&nbsp;&nbsp;&nbsp;&nbsp;&nbsp;Face sheet</p>
    <div class="art" role="img" aria-label="Illustration of a nurse" style="left:40px;top:120px;width:120px;height:110px;background:linear-gradient(#cfe3f7,#4d87d5)"></div>
  </aside>

  <!-- In patient step 3 -->
  <section class="abs step" style="top:1385px;height:970px">
    <div class="step-num">3</div>
    <div class="step-title">Evaluation</div>
    <p style="margin-top:14px">Evaluation of function level prior to discharge with Physical Therapist and Patient in Hospital</p>
    <ul style="margin-top:22px">
      <li>Patient notes and evaluation started</li>
      <li>Home evaluation planned with anticipated needs</li>
      <li>Preliminary introduction of three possible mobility solutions</li>
    </ul>
    <p style="margin:10px 0 0 30px">- &nbsp;Walking aids, manual wheelchair or power chair</p>
    <div class="art" role="img" aria-label="Illustration of a therapist beside a patient in a hospital bed" style="left:70px;top:470px;width:440px;height:200px;background:linear-gradient(#d8e8f8,#8bb7e8)"></div>
    <div class="art" role="img" aria-label="Illustration of a power wheelchair" style="left:100px;top:700px;width:170px;height:170px;background:#e6eef9"></div>
    <div class="art" role="img" aria-label="Illustration of a manual wheelchair" style="left:330px;top:700px;width:170px;height:170px;background:#e6eef9"></div>
    <p class="abs" style="left:140px;top:880px">power<br>chair</p>
    <p class="abs" style="left:365px;top:880px">manual<br>wheelchair</p>
  </section>
  <aside class="abs side" style="top:1390px">
    <h3>Reasons for custom and power wheelchairs vs. transport or standard wheelchair</h3>
    <ul style="margin-top:26px">
      <li><strong>Benefits of a Custom Wheelchair</strong>
        <p style="margin-left:10px">- K0005 Ultralight weight configurable wheelchair</p>
        <ul style="margin-left:40px">
          <li>Rear Axles can be placed 3" further forward to maximize leverage</li>
          <li>Adjustable posterior tilt of the seat and wheel camber will give better stability for residence ADL's</li>
        </ul>
      </li>
      <li style="margin-top:26px"><strong>Benefits of a Power Wheelchair</strong>
        <p style="margin-left:10px">- If patient can not propel a smaller base Power Wheel chair is a great solution</p>
        <ul style="margin-left:40px">
          <li>Group 3 PWC is only 24" wide which is 4 inches smaller than a manual wheelchair</li>
          <li>Can be configured with power tilt seat so patient can independently shirt positioning, reducing sitting pressure</li>
        </ul>
      </li>
    </ul>
  </aside>

  <!-- In patient step 4 -->
  <section class="abs step" style="top:2400px;height:345px">
    <div class="step-num">4</div>
    <div class="step-title">Prior to Patient Discharge</div>
    <ul style="width:290px">
      <li>Mobility Allies to bring "loaner" chair</li>
      <li>No charge invoice given to patient</li>
      <li>Transport Chair</li>
      <li>Standard Chair</li>
    </ul>
    <div class="art" role="img" aria-label="Illustration of a nurse pushing a patient in a wheelchair" style="left:340px;top:95px;width:250px;height:220px;background:linear-gradient(#d8e8f8,#8bb7e8)"></div>
  </section>

  <h2 class="abs section-head" style="left:60px;top:2800px">OUT PATIENT PROCESS</h2>

  <!-- Out patient step 1 -->
  <section class="abs step" style="top:2890px;height:590px">
    <p style="margin-top:60px">Ingress and egress issues within the residence. Looking for special obstacles such as split level floors, high thresh holds, furniture lay out or uneven exterior pathways. Access issues can cause possible issues with independent mobility and ADL's</p>
    <div class="art" role="img" aria-label="Illustration of a suburban house" style="left:110px;top:320px;width:420px;height:230px;background:linear-gradient(#d8e8f8,#8bb7e8)"></div>
  </section>
  <aside class="abs side" style="top:2895px">
    <h3>Important part of the process to determine how patient will use equipment in their own environment</h3>
    <ul style="margin-top:30px">
      <li style="padding-left:70px">Are there obstacles that need to be removed so patient can operate equipment for ADL's</li>
      <li style="padding-left:70px">Is a manual chair or power chair better for patient in their home environment</li>
      <li style="padding-left:70px">Measurements for door ways and thresholds</li>
      <li style="padding-left:70px">Community based activities</li>
    </ul>
  </aside>

  <!-- Out patient step 2 -->
  <section class="abs step" style="top:3515px;height:345px">
    <div class="step-num">2</div>
    <div class="step-title">Final Out Patient Therapy evaluation</div>
    <ul style="width:330px">
      <li>Evaluation with Physical therapist for final optimal seating and mobility equipment based on all the findings.</li>
    </ul>
    <div class="art" role="img" aria-label="Illustration of two therapists" style="left:390px;top:90px;width:210px;height:230px;background:linear-gradient(#d8e8f8,#8bb7e8)"></div>
  </section>
  <aside class="abs side" style="top:3520px">
    <h3>Notes from evaluation submitted to therapist which include</h3>
    <ol style="list-style:none;margin:20px 0 0 34px">
      <li>a) &nbsp;Seating mobility issues to be addressed</li>
      <li>b) &nbsp;Equipment considered and not chosen with rationale</li>
      <li>c) &nbsp;Equipment recommended and why client requires each item</li>
      <li>d) &nbsp;Expected outcome</li>
    </ol>
  </aside>

  <!-- Out patient step 3 -->
  <section class="abs step" style="top:3920px;height:610px">
    <div class="step-num">3</div>
    <div class="step-title">Completion of final documentation and compliance review</div>
    <ul>
      <li>Therapist reviews all notes and combines with PT evaluation to create Letter of Medical Justification</li>
      <li>Letter is signed and submitted to patients MD for patient face to face visit and modifications or con</li>
      <li>All paperwork is submitted for payor approval</li>
      <li>Equipment is ordered</li>
      <li>Equipment is assembled to patient recommended configuration</li>
    </ul>
    <div class="art" role="img" aria-label="Illustration of paperwork with a pen" style="left:150px;top:440px;width:300px;height:140px;background:linear-gradient(#eef4fb,#b9d3f1)"></div>
  </section>

  <!-- Out patient step 4 -->
  <section class="abs step" style="top:4580px;height:375px">
    <div class="step-num">4</div>
    <div class="step-title">Delivery of Custom Equipment</div>
    <p style="margin-top:20px">Payor final approval</p>
    <div class="art" role="img" aria-label="Illustration of a delivery truck" style="left:70px;top:190px;width:260px;height:160px;background:linear-gradient(#eef4fb,#b9d3f1)"></div>
  </section>
  <aside class="abs side" style="top:4585px">
    <h3>Equipment is delivered, fit and operational training</h3>
    <ul style="margin-top:30px">
      <li>Review equipment with patient</li>
      <li>Verify that equipment is configured correctly and adjustments made if necessary</li>
      <li>Happy Patient</li>
    </ul>
    <div class="art" role="img" aria-label="Illustration of a happy patient" style="left:300px;top:270px;width:120px;height:120px;background:linear-gradient(#d8e8f8,#8bb7e8)"></div>
  </aside>

  <div class="abs stripe" style="top:5030px;height:40px"></div>
</body>
</html>
```